Fitness Training academy needs a business card design

We need a business card design for a NEW business that teaches/trains people how to become personal trainers. We would like to see designs both with and without our QR code. We would like our designs double sided.

See the following attachments
Design Brief
Logos (both black background, white background in all formats)
QR Code

```html
<!DOCTYPE html>
<html lang="en">
<head>
<meta charset="utf-8">
<title>Elevate Strength Institute – Business Card</title>
<link rel="stylesheet" href="https://fonts.googleapis.com/css2?family=Exo+2:wght@400;500;600&display=swap">
<style>
  :root {
    --backdrop: #d9d6d2;
    --card: #ffffff;
    --card-shade: #eeeeee;
    --orange-light: #f7931e;
    --orange: #f26a21;
    --red: #e43d1b;
    --swoosh: #2b2b2b;
    --ink: #333333;
    --ink-soft: #555555;
    --white: #ffffff;
  }
  * { box-sizing: border-box; margin: 0; padding: 0; }
  html, body {
    width: 1200px; height: 899px; overflow: hidden;
    background: var(--backdrop);
    font-family: "Exo 2", sans-serif;
  }
  .card {
    position: absolute; left: 100px; top: 164px;
    width: 1000px; height: 571px;
    border-radius: 56px; overflow: hidden;
    background: linear-gradient(160deg, var(--card) 40%, var(--card-shade));
    box-shadow: 0 18px 40px rgba(0,0,0,.25);
  }
  .card__band { position: absolute; inset: 0; }
  .card__holder {
    position: absolute; right: 60px; top: 92px;
    text-align: right; color: var(--white);
  }
  .card__name { font-size: 32px; font-weight: 500; letter-spacing: 1px; }
  .card__role { font-size: 22px; margin-top: 6px; }
  .brand {
    position: absolute; left: 56px; top: 118px;
    display: flex; align-items: center; gap: 18px;
  }
  .brand__mark {
    width: 96px; height: 96px; border-radius: 50%;
    background: var(--orange);
  }
  .brand__name {
    font-size: 26px; font-weight: 600; color: var(--ink-soft);
    letter-spacing: .5px; text-transform: uppercase;
  }
  .contacts {
    position: absolute; left: 60px; top: 290px;
    list-style: none;
  }
  .contacts li {
    display: flex; align-items: center; gap: 14px;
    height: 38px; font-size: 22px; color: var(--ink);
  }
  .contacts svg { width: 22px; height: 22px; fill: var(--orange); }
  .address {
    position: absolute; right: 70px; bottom: 42px;
    text-align: right; font-size: 24px; line-height: 36px; color: var(--ink);
  }
</style>
</head>
<body>
  <section class="card">
    <svg class="card__band" viewBox="0 0 1000 571" preserveAspectRatio="none" aria-hidden="true">
      <defs>
        <linearGradient id="bandFill" x1="0" y1="0" x2="1" y2="0.4">
          <stop offset="0" stop-color="var(--red)"/>
          <stop offset="0.5" stop-color="var(--orange-light)"/>
          <stop offset="1" stop-color="var(--red)"/>
        </linearGradient>
      </defs>
      <path d="M0 0 H1000 V470 C880 210 560 60 0 70 Z" fill="var(--swoosh)"/>
      <path d="M0 0 H1000 V440 C870 200 540 52 0 58 Z" fill="url(#bandFill)"/>
    </svg>

    <div class="card__holder">
      <p class="card__name">DANIEL WHITMORE</p>
      <p class="card__role">Managing Director</p>
    </div>

    <div class="brand">
      <span class="brand__mark"></span>
      <span class="brand__name">Elevate Strength Institute</span>
    </div>

    <ul class="contacts">
      <li><svg viewBox="0 0 24 24"><path d="M6.6 10.8a15 15 0 0 0 6.6 6.6l2.2-2.2a1 1 0 0 1 1-.25 11.4 11.4 0 0 0 3.6.6 1 1 0 0 1 1 1V20a1 1 0 0 1-1 1A17 17 0 0 1 3 4a1 1 0 0 1 1-1h3.5a1 1 0 0 1 1 1c0 1.25.2 2.45.6 3.6a1 1 0 0 1-.25 1Z"/></svg>021 555 0147</li>
      <li><svg viewBox="0 0 24 24"><path d="M7 1h10a2 2 0 0 1 2 2v18a2 2 0 0 1-2 2H7a2 2 0 0 1-2-2V3a2 2 0 0 1 2-2Zm0 3v14h10V4Zm5 15.5a1.2 1.2 0 1 0 0 2.4 1.2 1.2 0 0 0 0-2.4Z"/></svg>021 555 0148</li>
      <li><svg viewBox="0 0 24 24"><path d="M6 2h9l3 3v5H6Zm-3 9h18v9H3Zm3 2v2h4v-2Zm7 0v2h5v-2Z"/></svg>021 555 0149</li>
      <li><svg viewBox="0 0 24 24"><path d="M2 5h20v14H2Zm2 2v.5l8 5.5 8-5.5V7Zm0 3v7h16v-7l-8 5.5Z"/></svg>hello@elevatestrength.net</li>
      <li><svg viewBox="0 0 24 24"><path d="M12 2a10 10 0 1 0 0 20 10 10 0 0 0 0-20Zm-1 2.1V11H4.1A8 8 0 0 1 11 4.1Zm2 0A8 8 0 0 1 19.9 11H13Zm-8.9 8.9H11v6.9A8 8 0 0 1 4.1 13Zm8.9 0h6.9A8 8 0 0 1 13 19.9Z"/></svg>www.elevatestrength.net</li>
    </ul>

    <p class="address">214, 9th floor, Crestview<br>Tower Road</p>
  </section>
</body>
</html>
```